quiet meadow therapy (QMT)

I need to build a website for my therapy business.
There are two parts to the website
on the landing page; they choose whether they are therapists making a referral or patients needing more information.
After that, they are taken to their respective pages.
There is the textual information and a referral form on the therapist page, and on the patient page, the text is a bit different, and there will be a booking page on the patient page.
Visually minimal, it's a therapeutic website. I want it clean, clinical, and modern
colors: greenish blue or maybe orangish
PHP/html code
Updates

Hi everyone
I'm very sorry for the lack of responses to your designs. I am trying to work it out, but this platform has been a challenge for me.
I appreciate everyone's efforts, and I am unsure how to rate designs and move forward with the ones I like. There is a 5-star rating, but I don't understand how I'm supposed to politely say that it is not it without feeling like I'm going to affect someone's future rating negatively.
Please understand me. Thank you

Designs look the same

Target Market(s)

therapy and stress management

Industry/Entity Type

stress management therapy

Coding

Coded - Design and coding required

Number of Pages Required

5+ page

Font styles to use
Serif

Colors
0094D4
00A9DD
6FCCEA
C7EBF8
E9F6FB
00AB8E
00BBA5
67D7C9
C6EFE9
E9F9F6

Requirements
Must have
• landing page that that have 2 options. one for therapist another for patient

```html
<!DOCTYPE html>
<html lang="en">
<head>
<meta charset="utf-8">
<title>QMT — Quiet Meadow Therapy</title>
<link href="https://fonts.googleapis.com/css2?family=Alex+Brush&family=Poppins:wght@400;500;600;700;800&family=Roboto:wght@400;500;700&display=swap" rel="stylesheet">
<style>
:root{
  --teal:#00bba5;
  --teal-dark:#00ab8e;
  --teal-light:#c6efe9;
  --teal-soft:#67d7c9;
  --orange:#f7941d;
  --ink:#1c1c1c;
  --grey-bg:#f2f2f2;
  --dark:#262626;
  --white:#ffffff;
}
*{box-sizing:border-box;margin:0;padding:0}
html,body{width:1200px;height:4071px;overflow:hidden}
body{position:relative;font-family:"Roboto",Arial,sans-serif;color:var(--ink);background:var(--white)}
.abs{position:absolute}
.script{font-family:"Alex Brush",cursive;font-weight:400}
.head{font-family:"Poppins",Arial,sans-serif}

/* header */
.site-header{left:0;top:0;width:1200px;height:116px;background:#f8fbfb}
.brand{left:110px;top:32px;display:flex;align-items:center;gap:12px}
.brand-dot{width:34px;height:34px;border-radius:50%;background:var(--teal)}
.brand-name{font-family:"Poppins",sans-serif;font-weight:500;font-size:38px;letter-spacing:10px;color:#333}
.main-nav{left:361px;top:40px;width:418px;height:40px;border-top:1.5px solid #555;border-bottom:1.5px solid #555;display:flex;justify-content:space-around;align-items:center}
.main-nav a{font-family:"Poppins",sans-serif;font-weight:600;font-size:13px;color:#222;text-decoration:none;position:relative}
.main-nav a.active{color:var(--teal)}
.main-nav a.active::after{content:"";position:absolute;left:0;right:0;bottom:-9px;height:2px;background:var(--teal)}
.btn-book-top{left:903px;top:41px;width:185px;height:39px;background:var(--orange);color:#fff;font-family:"Poppins",sans-serif;font-weight:600;font-size:13px;display:flex;align-items:center;justify-content:center;border-radius:2px}

/* photo placeholders */
.photo-fill{position:absolute}

/* hero */
.hero{left:0;top:116px;width:1200px;height:578px;overflow:hidden}
.hero-photo{inset:0;background:
  linear-gradient(90deg,#e9e6e2 0%,#ddd6cf 40%,#5b4088 62%,#4a336f 78%,#6f6356 100%)}
.hero-circle{position:absolute;left:-24px;top:193px;width:488px;height:488px;border-radius:50%;background:var(--teal)}
.hero-title{left:111px;top:296px;font-size:28px;font-weight:700;color:#fff;line-height:32px;font-family:"Poppins",sans-serif;letter-spacing:.5px}
.hero-rule{left:111px;top:370px;width:80px;height:3px;background:var(--orange)}
.hero-text{left:111px;top:388px;width:320px;font-family:"Poppins",sans-serif;font-size:11.5px;line-height:23px;color:#fff}
.path-label{left:112px;top:462px;font-family:"Poppins",sans-serif;font-size:11px;font-weight:500;color:#fff;letter-spacing:.4px}
.hero-choice{left:112px;top:484px;display:flex;gap:10px}
.choice{height:34px;padding:0 16px;font-family:"Poppins",sans-serif;font-weight:600;font-size:11px;display:flex;align-items:center;justify-content:center}
.choice.solid{background:#fff;color:var(--teal)}
.choice.outline{border:1.5px solid #fff;color:#fff}
.dots{left:590px;top:531px;display:flex;gap:4px}
.dots span{width:20px;height:20px;border-radius:50%;background:#fff}
.dots span:first-child{background:var(--teal)}

/* why */
.why{left:0;top:694px;width:1200px;height:726px;background:var(--grey-bg)}
.mark{width:50px;height:70px;border-radius:50%;background:var(--teal-soft)}
.why-title{left:0;width:1200px;top:100px;text-align:center;display:flex;justify-content:center;align-items:baseline;gap:6px}
.why-title .script{font-size:48px;color:#222}
.why-title .head{font-size:34px;font-weight:700;color:var(--teal)}
.why-lead{left:0;width:1200px;top:170px;text-align:center;font-size:19px;line-height:26px;color:#222;letter-spacing:.3px;font-weight:400}
.feature{width:289px;height:289px;border:3px solid var(--teal);border-radius:50%;display:flex;flex-direction:column;align-items:center;padding-top:38px;text-align:center}
.feature svg{width:70px;height:70px;stroke:var(--teal);fill:none;stroke-width:2.2}
.feature h3{font-family:"Poppins",sans-serif;font-weight:600;font-size:20px;color:var(--teal);margin-top:14px}
.feature p{font-size:18px;line-height:24px;width:190px;margin-top:8px}
.btn-teal{background:var(--teal);color:#fff;font-family:"Poppins",sans-serif;font-weight:600;display:flex;align-items:center;justify-content:center;border-radius:3px}

/* best therapist */
.best{left:0;top:1420px;width:1200px;height:721px}
.best-panel{left:0;top:0;width:529px;height:721px;background:var(--teal)}
.best-photo{left:529px;top:0;width:671px;height:721px;background:linear-gradient(90deg,#2e2c2b 0%,#3b3531 30%,#8a6852 60%,#b08a70 75%,#5c4f46 100%)}
.best-mark{left:245px;top:107px;width:60px;height:83px;border-radius:50%;background:#fff}
.best-script{left:0;width:529px;top:200px;text-align:center;font-size:72px;color:#111}
.best-title{left:0;width:529px;top:303px;text-align:center;font-family:"Poppins",sans-serif;font-weight:800;font-size:56px;color:#fff;letter-spacing:1px}
.best-text{left:111px;top:404px;width:400px;font-size:19px;line-height:26px;color:#fff}
.best-btn{left:145px;top:533px;width:283px;height:57px;background:#f3f7f6;color:var(--teal);font-family:"Poppins",sans-serif;font-weight:500;font-size:18px;display:flex;align-items:center;justify-content:center}

/* services */
.svc{display:flex;flex-direction:column;align-items:center;text-align:center;padding-top:38px}
.svc svg{width:60px;height:50px;stroke:#222;fill:none;stroke-width:2}
.svc h4{font-family:"Poppins",sans-serif;font-weight:600;font-size:17px;letter-spacing:.8px;margin-top:22px;color:#1c1c1c}
.svc p{font-size:10.5px;color:#444;margin-top:10px}
.svc.light{background:var(--teal-light)}
.svc.plain{background:#fff}

/* benefits */
.benefits{left:0;top:2618px;width:1200px;height:812px;background:#fff}
.ben-title{left:0;width:1200px;top:120px;display:flex;justify-content:center;align-items:center;gap:18px}
.ben-title .script{font-size:80px;color:#111}
.ben-title .head{font-size:56px;font-weight:800;color:var(--teal);letter-spacing:1px}
.ben-photo{left:300px;top:300px;width:600px;height:360px;border-radius:45% 45% 8px 8px;background:linear-gradient(180deg,#f5e6dc 0%,#e9c9b3 55%,#f6ece6 100%)}
.tag{height:33px;background:var(--teal);color:#fff;font-family:"Roboto",sans-serif;font-weight:500;font-size:20px;display:flex;align-items:center;padding:0 12px;white-space:nowrap}
.tag::after{content:"";position:absolute;bottom:-10px;border-left:10px solid transparent;border-top:10px solid var(--teal)}
.tag.r::after{right:14px}
.tag.l::after{left:14px;border-left:0;border-right:10px solid transparent}
.ben-btn{left:423px;top:709px;width:350px;height:56px;font-size:18px;border-radius:0}

/* contact */
.contact{left:0;top:3430px;width:1200px;height:575px;background:var(--dark);color:#fff}
.contact-script{left:0;width:1200px;top:18px;text-align:center;font-size:32px}
.contact-title{left:0;width:1200px;top:62px;text-align:center;font-family:"Poppins",sans-serif;font-weight:600;font-size:27px;letter-spacing:1.5px}
.contact-rule{left:556px;top:116px;width:64px;height:4px;background:#fff}
.field{width:307px;height:36px;border:1.5px solid #bbb;border-radius:3px;font-family:"Poppins",sans-serif;font-size:12px;color:#ddd;padding:8px 10px}
.field.area{width:308px;height:148px}
.submit{left:519px;top:370px;width:128px;height:35px;border-radius:18px;font-size:12px;font-weight:500}
.info{top:465px;width:300px;text-align:center;font-family:"Poppins",sans-serif;font-size:12px;line-height:22px;font-weight:500}

/* footer */
.site-footer{left:0;top:4005px;width:1200px;height:66px;background:#fff}
.copy{left:165px;top:26px;font-family:"Poppins",sans-serif;font-size:11.5px;color:#222}
.socials{left:865px;top:16px;display:flex;gap:3px}
.socials span{width:34px;height:34px;border-radius:3px}
</style>
</head>
<body>

<header class="site-header abs">
  <div class="brand abs"><span class="brand-dot"></span><span class="brand-name">QMT</span></div>
  <nav class="main-nav abs">
    <a class="active">HOME</a><a>ABOUT</a><a>SERVICES</a><a>BLOG</a><a>CONTACT</a>
  </nav>
  <div class="btn-book-top abs">BOOK APPOINTMENT</div>
</header>

<section class="hero abs">
  <div class="photo-fill hero-photo" role="img" aria-label="Photo of a therapist comforting a young male patient in a bright room"></div>
  <div class="hero-circle"></div>
  <h1 class="hero-title abs">Increase Stress<br>Resistance?</h1>
  <div class="hero-rule abs"></div>
  <p class="hero-text abs">Lorem Ipsum is simply dummy text of the printing and typesetting industry. Lorem Ipsum has been the industry's standard dummy text ever since the 1500s</p>
  <p class="path-label abs">Choose your path:</p>
  <div class="hero-choice abs">
    <a class="choice solid">I'm a Therapist</a>
    <a class="choice outline">I'm a Patient</a>
  </div>
  <div class="dots abs"><span></span><span></span><span></span><span></span></div>
</section>

<section class="why abs">
  <div class="mark abs" style="left:575px;top:28px"></div>
  <h2 class="why-title abs"><span class="script">Why</span><span class="head">QMT?</span></h2>
  <p class="why-lead abs">Lorem ipsum dolor sit amet, consectetur adipiscing elit.<br>Vivamus lacinia odio vitae vestibulum vestibulum.</p>

  <div class="feature abs" style="left:64px;top:264px">
    <svg viewBox="0 0 70 70" role="img" aria-label="Therapy table icon"><rect x="6" y="34" width="40" height="6"/><path d="M10 40v18M42 40v18"/><circle cx="32" cy="24" r="5"/><circle cx="56" cy="16" r="6"/><path d="M50 26h12v22M50 26v8"/></svg>
    <h3>Trained Therapists</h3>
    <p>Lorem ipsum dolor sit amet</p>
  </div>
  <div class="feature abs" style="left:453px;top:264px">
    <svg viewBox="0 0 70 70" role="img" aria-label="Clinic building icon"><rect x="14" y="10" width="42" height="52"/><path d="M35 16v12M29 22h12"/><rect x="20" y="34" width="8" height="8"/><rect x="42" y="34" width="8" height="8"/><rect x="30" y="48" width="10" height="14"/><path d="M6 62h58"/></svg>
    <h3>Fully Equipped Clinic</h3>
    <p>Lorem ipsum dolor sit amet</p>
  </div>
  <div class="feature abs" style="left:845px;top:264px">
    <svg viewBox="0 0 70 70" role="img" aria-label="Personal care search icon"><circle cx="30" cy="24" r="12"/><path d="M14 56c0-12 8-18 16-18"/><circle cx="46" cy="46" r="9"/><path d="M53 53l8 8"/></svg>
    <h3>Personalised Treatment</h3>
    <p>Lorem ipsum dolor sit amet</p>
  </div>

  <div class="btn-teal abs" style="left:446px;top:600px;width:306px;height:68px;font-size:18px">LEARN MORE</div>
</section>

<section class="best abs">
  <div class="best-panel abs"></div>
  <div class="best-photo abs" role="img" aria-label="Photo of a woman meditating with eyes closed"></div>
  <div class="best-mark abs"></div>
  <div class="best-script script abs">Best</div>
  <h2 class="best-title abs">THERAPIST</h2>
  <p class="best-text abs">Lorem ipsum dolor sit amet, consectetur adipiscing elit. Vivamus lacinia odio vitae vestibulum vestibulum.</p>
  <div class="best-btn abs">Book Now</div>
</section>

<div class="abs" style="left:0;top:2141px;width:598px;height:238px;background:linear-gradient(90deg,#3a2a22 0%,#7d5a47 40%,#c9a58c 70%,#e6d4c6 100%)" role="img" aria-label="Photo of a woman receiving a relaxing head massage"></div>
<div class="svc light abs" style="left:598px;top:2141px;width:298px;height:238px">
  <svg viewBox="0 0 60 50" role="img" aria-label="Lotus icon"><path d="M30 8c-6 8-6 18 0 28 6-10 6-20 0-28zM30 36c-8-4-16-10-18-20 8 2 14 8 18 20zM30 36c8-4 16-10 18-20-8 2-14 8-18 20zM6 34c8 6 16 4 24 2 8 2 16 4 24-2"/></svg>
  <h4>PATIENT RELAXATION</h4>
  <p>Lorem ipsum dolor sit amet, consectetur a ipsum</p>
</div>
<div class="svc plain abs" style="left:896px;top:2141px;width:304px;height:238px">
  <svg viewBox="0 0 60 50" role="img" aria-label="Mortar and pestle icon"><path d="M10 20h40c0 14-8 22-20 22S10 34 10 20z"/><path d="M22 44h16M36 18l14-14"/><circle cx="46" cy="10" r="3"/></svg>
  <h4>PATIENT DETOXIFICATION</h4>
  <p>Lorem ipsum dolor sit amet, consectetur a ipsum</p>
</div>
<div class="svc light abs" style="left:0;top:2379px;width:279px;height:239px">
  <svg viewBox="0 0 60 50" role="img" aria-label="Hands icon"><path d="M8 36c10-2 16-8 22-16 4-6 12-8 18-4M14 42c10 0 20-6 26-12 4-4 10-4 12 0"/></svg>
  <h4>PATIENT STRESS THERAPY</h4>
  <p>Lorem ipsum dolor sit amet, consectetur a ipsum</p>
</div>
<div class="svc plain abs" style="left:279px;top:2379px;width:318px;height:239px">
  <svg viewBox="0 0 60 50" role="img" aria-label="Oil drop over hand icon"><path d="M30 4c-4 6-6 9-6 12a6 6 0 0 0 12 0c0-3-2-6-6-12z" fill="#222"/><path d="M8 34c8 0 14 2 20 4 8 0 16-4 22-8M8 44c12 2 24 2 36-6"/></svg>
  <h4>PATIENT OIL THERAPY</h4>
  <p>Lorem ipsum dolor sit amet, consectetur a ipsum</p>
</div>
<div class="abs" style="left:597px;top:2379px;width:603px;height:239px;background:linear-gradient(90deg,#ece8e2 0%,#d8cfc4 40%,#4a4440 65%,#e2dccf 90%)" role="img" aria-label="Photo of a therapist showing happy and sad face cards to a child"></div>

<section class="benefits abs">
  <div class="mark abs" style="left:570px;top:37px"></div>
  <h2 class="ben-title abs"><span class="script">Benefits For</span><span class="head">PATIENT</span></h2>
  <div class="ben-photo abs" role="img" aria-label="Photo of a woman resting her head on her arms beside a pink lotus flower"></div>
  <div class="tag r abs" style="left:155px;top:254px">It counteracts all that sitting you do</div>
  <div class="tag l abs" style="left:727px;top:254px">It soothes anxiety and depression</div>
  <div class="tag r abs" style="left:110px;top:350px">It eases muscle pain</div>
  <div class="tag l abs" style="left:873px;top:350px">It boosts immunity</div>
  <div class="tag r abs" style="left:104px;top:451px">It relieves headaches</div>
  <div class="tag l abs" style="left:818px;top:451px">It improves sleep</div>
  <div class="btn-teal ben-btn abs">Book Now For Patient</div>
</section>

<section class="contact abs">
  <div class="contact-script script abs">Leave a message</div>
  <h2 class="contact-title abs">GET IN TOUCH</h2>
  <div class="contact-rule abs"></div>
  <div class="field abs" style="left:268px;top:190px">Your Name</div>
  <div class="field abs" style="left:268px;top:245px">Your Email</div>
  <div class="field abs" style="left:268px;top:299px">Your Phone</div>
  <div class="field area abs" style="left:602px;top:190px">Your Message</div>
  <div class="btn-teal submit abs">Submit</div>
  <div class="info abs" style="left:100px">Call Us<br>000-0000-000000</div>
  <div class="info abs" style="left:436px">Address<br>Lorem Ipsum is simply dummy text of the</div>
  <div class="info abs" style="left:769px">Email Us<br>hello@quietmeadow.example</div>
</section>

<footer class="site-footer abs">
  <p class="copy abs">© 2022 QMT – ALL RIGHTS RESERVED. PRIVACY POLICY</p>
  <div class="socials abs" aria-label="Social links">
    <span style="background:#3b5a9a"></span><span style="background:#1da1f2"></span><span style="background:#c13584"></span><span style="background:#0a66c2"></span>
  </div>
</footer>

</body>
</html>
```